Web Design (Coded) and Project - Finance Company

Tallowen Lending Group is a mortgage broker company based in Sydney Australia and provides lending solutions for individuals and businesses.

Our target market is anyone with the financial means to get a loan.

I am looking for a website design in this contest. The site needs to be able to be viewed on a portable device such as Veltab, Velfon, etc.

I have the logo design and files which need to be used. I also have the BLQR logo which will need to be in the footer of each page.

The website needs to represent a big finance company with integrity and knowledge.

The website will need to be uploaded to Pelwickhost.com.au as they are the hosting provider. I will also need the ability to make changes to the text and pictures in the future and upload the revisions. I need the website ready to go and ready to be uploaded onto Pelwick Host.

The website will consist of 6 pages in total There are 4 main pages that will be viewed and then 2 with Privacy and Internal Dispute Resolution which are only accessed through links. These will be as follows:

Home
I would prefer to have a fresh bright and professional looking home page given that most mortgage broker websites look the same with the menu buttons at the top.

Services
Details the loan types that we handle and some text for each one.

About Us
I have the text for this.

Contact Us
Form to have the following inputs:
• Surname
• First Name
• Suburb
• State
• Phone number
• Mobile number
• Email address
• Preferred contact
o Phone
o Mobile
o Email
• Reason for Enquiry
o First home buyer
o Refinance
o Investment Property
o Commercial lending
o Personal loan
o Other
• Comments

Privacy
This page will only be accessed from a link at the bottom of each page. I have the wording that I will provide.

Dispute Resolution Policy
This page will only be accessed from a link on the Contact Us page. I have the wording that I will provide.
Updates

The designs that are coming through so far are generally looking the same generic website layout. I am looking for the home page to be something different with more of a wow factor and something different to the standard page link menu accross the top of the screen. The content should be fairly minimal given that I am a new business there will be limited text for each page. I am happy to increase the budget if required as I appreciate there will be more work involved.

Reason: I am extending the deadline as the design so far are good but fairly generic and template style home pages. For the home page I am looking for something a little more striking with a visual impact.

I have increased the payment by $200 to encourage more designs. Designs need to be relevant to the business, the number of pages and content. Several designs have come through looking good but just look like a standard template with my logo added, but the content does not match the business.

The brief stated that I am looking for the home page to be something different with more of a wow factor and something different to the standard page link menu accross the top of the screen. All of the designs have come through with the navigation bar along the top and a generic layout. I have attached a couple of idea's. Obviously these do not relate to the finance and mortgage industry but you can see the sort of style that gives the site a wow factor. The other pages can be more generic, but the first page is the attention grabber. You can also see the VelFon view that I am after. These are just templates from Pelwick Host that I could use to build the site, I just don't have the time or creative flair. Please submit more designs. Thanks for your work to date, Rob.

Hi. Could you please submit designs based on brief and the two screen shots attached. Mobile device view should work as per screen shots. Thanks, Rob

Reason: Still looking for designs to meet the brief provided.

Industry/Entity Type

Financial

Requirements
Must have
• Colour palette to be as supplied. I will post this shortly.
Should not have
• No cheesy smiley faces
No handshaking
No money pictures
No pictures of stones
No picture of people in an office looking at things
No lime green or purple in colour
Would prefer not to have a picture of the Corvell Arch or Marlow Hall

```html
<!DOCTYPE html>
<html lang="en">
<head>
<meta charset="utf-8">
<title>Tallowen Lending Group</title>
<link href="https://fonts.googleapis.com/css2?family=Arimo:wght@400;700&display=swap" rel="stylesheet">
<style>
:root{
  --blue:#0c8fcf;
  --blue-dark:#0a6ea3;
  --navy:#1d4d73;
  --orange:#f7941d;
  --orange-light:#ffb12e;
  --text:#333;
  --muted:#888;
  --line:#e2e2e2;
}
*{box-sizing:border-box;margin:0;padding:0}
html,body{width:1200px;height:948px;overflow:hidden;background:#fff}
body{position:relative;font-family:"Arimo",Arial,sans-serif;color:var(--text);font-size:10px}
a{text-decoration:none;color:inherit}

/* header */
.brand{position:absolute;left:248px;top:18px;display:flex;align-items:center;gap:10px}
.brand-mark{width:48px;height:48px;border-radius:50%;background:var(--blue)}
.brand-name{font-weight:700;font-size:15px;line-height:15px;color:#2b3a4a;text-transform:uppercase}
.contact{position:absolute;left:520px;top:20px;width:212px;text-align:right}
.phone{color:var(--blue);font-size:28px;line-height:30px}
.phone small{font-size:11px;vertical-align:top;margin-right:8px}
.email{font-size:10px;font-weight:700;color:#444;margin-top:4px}

/* hero */
.hero{position:absolute;left:232px;top:86px;width:752px;height:320px;border-bottom:1px solid #ccc;border-right:1px solid #eee;border-top:1px solid #ddd}
.hero-divider{position:absolute;left:200px;top:0;width:1px;height:305px;background:var(--line)}
.main-nav{position:absolute;left:214px;top:97px;width:201px;box-shadow:0 2px 4px rgba(0,0,0,.2)}
.main-nav a{display:flex;align-items:center;height:52px;padding-left:20px;gap:17px;color:#fff;font-weight:700;font-size:12px;text-shadow:0 1px 1px rgba(0,0,0,.35);background:linear-gradient(#54bde8,#1e9ad3);border-bottom:2px solid #0d6c9b}
.main-nav a:first-child{background:linear-gradient(#b3e3f6,#6fc7ea)}
.main-nav a:last-child{border-bottom:0}
.main-nav svg{width:14px;height:14px;fill:var(--navy)}
.promo{position:absolute;left:248px;top:310px;width:167px;height:81px;background:linear-gradient(#fff,#f0f0f0);box-shadow:0 1px 3px rgba(0,0,0,.2);padding:10px 10px 0 21px}
.promo::before{content:"";position:absolute;left:10px;top:12px;width:2px;height:56px;background:var(--orange)}
.promo h3{font-weight:400;font-size:12px;color:var(--navy);margin-bottom:4px}
.promo p{font-size:9px;line-height:14.4px;text-align:justify}
.slide-photo{position:absolute;left:640px;top:87px;width:344px;height:318px;background:linear-gradient(90deg,#fff 0%,#f1ece8 25%,#e7d3c4 60%,#d9c1b0 100%)}
.slide-title{position:absolute;left:468px;top:110px;font-size:48px;line-height:49px;font-weight:400;color:var(--orange)}
.slide-rule{position:absolute;left:471px;top:221px;width:84px;height:1px;background:#ccc}
.slide-text{position:absolute;left:471px;top:240px;font-size:21px;line-height:24px;color:#666}
.btn-orange{position:absolute;left:470px;top:337px;width:166px;height:28px;border-radius:14px;background:linear-gradient(var(--orange-light),var(--orange));color:#fff;font-weight:700;font-size:10px;line-height:28px;padding-left:16px;box-shadow:0 1px 2px rgba(0,0,0,.3)}
.btn-orange::after{content:"›";position:absolute;right:14px;font-size:13px}
.dots{position:absolute;left:914px;top:377px;display:flex;gap:7px}
.dots i{width:8px;height:8px;border-radius:50%;background:#eee;box-shadow:inset 0 1px 1px rgba(0,0,0,.2)}
.dots i.on{background:var(--orange)}

/* news */
.news{position:absolute;left:232px;top:420px;width:752px;height:142px;border-bottom:1px solid var(--line)}
.news-intro{position:absolute;left:0;top:0;width:146px;height:142px;border-right:1px solid var(--line);text-align:center}
.news-intro svg{margin-top:14px;width:24px;height:24px}
.section-title{font-weight:400;font-size:22px;color:var(--orange)}
.news-intro .section-title{margin-top:6px}
.btn-grey{position:absolute;left:26px;top:96px;width:94px;height:24px;border-radius:12px;background:linear-gradient(#f4f4f4,#d8d8d8);box-shadow:0 1px 2px rgba(0,0,0,.25);font-weight:700;font-size:10px;line-height:24px;color:#333;text-align:left;padding-left:14px}
.btn-grey::after{content:"›";position:absolute;right:12px;color:#888}
.news-item{position:absolute;top:10px;width:290px;height:130px}
.news-item-first{left:162px}
.news-item-second{left:469px}
.news-sep{position:absolute;left:449px;top:0;width:1px;height:142px;background:var(--line)}
.thumb{position:absolute;left:0;top:0;width:66px;height:64px;background:linear-gradient(135deg,#c9d3db,#5e6b78);box-shadow:0 1px 2px rgba(0,0,0,.3)}
.thumb.alt{background:linear-gradient(135deg,#8fd0f2,#3b8ec2)}
.news-body{position:absolute;left:79px;top:0;width:190px}
.date{font-size:9px;color:var(--muted)}
.item-title{font-size:11px;font-weight:700;color:var(--blue);margin:2px 0 9px;white-space:nowrap}
.news-body p{font-size:9.5px;line-height:14.4px;text-align:justify;width:190px}
.more{display:inline-block;margin-top:14px;font-weight:700;font-size:10px;color:var(--navy)}
.more::after{content:"›";margin-left:8px;color:var(--blue)}

/* services */
.services-title{position:absolute;left:246px;top:574px}
.service{position:absolute;top:614px;width:232px}
.service-one{left:247px}
.service-two{left:492px}
.service-three{left:737px}
.service-photo{height:80px;background:linear-gradient(90deg,#c6cfd6,#7d8d9b)}
.service-photo.warm{background:linear-gradient(90deg,#efe3d8,#d8b79d)}
.service-photo.cool{background:linear-gradient(90deg,#5a6e88,#b9c6d3)}
.service h3{font-size:11px;font-weight:700;color:var(--blue);margin:13px 0 0 23px;position:relative;white-space:nowrap}
.service h3::before{content:"›";position:absolute;left-13px;left:-13px;color:#8ab}
.service p{font-size:9.5px;line-height:14.4px;margin:11px 6px 0 9px;text-align:justify}
.services-rule{position:absolute;left:232px;top:787px;width:752px;height:1px;background:var(--line)}

/* partners */
.partners{position:absolute;left:246px;top:800px;width:730px;height:64px;display:flex;align-items:center}
.partners-label{font-size:14px;color:#777;width:114px}
.partner{font-weight:700;font-size:20px;color:#bbb;width:154px;text-align:center;white-space:nowrap}

/* footer */
.site-footer{position:absolute;left:0;top:874px;width:1200px;height:74px;background:linear-gradient(#e3eef5,#f4f9fc);border-top:1px solid #cfdde6}
.badge{position:absolute;left:246px;top:18px;width:92px;height:36px;border:2px solid var(--navy);border-radius:3px;background:#fff}
.footer-nav{position:absolute;left:366px;top:22px;display:flex;font-size:9px;font-weight:700;color:var(--blue)}
.footer-nav a{padding:0 12px;border-left:1px solid #b9cfdc}
.footer-nav a:first-child{padding-left:0;border:0}
.copyright{position:absolute;left:366px;top:41px;font-size:9px;font-weight:700;color:#777}
.to-top{position:absolute;left:909px;top:31px;font-size:9px;font-weight:700;color:#777}
.to-top::after{content:"›";display:inline-block;transform:rotate(-90deg);margin-left:8px;color:var(--blue)}
</style>
</head>
<body>

<header>
  <div class="brand">
    <span class="brand-mark"></span>
    <span class="brand-name">Tallowen<br>Lending<br>Group</span>
  </div>
  <div class="contact">
    <div class="phone"><small>+61</small>0 755 318 204</div>
    <div class="email">contact@tallowenlending.com</div>
  </div>
</header>

<section class="hero">
  <div class="hero-divider"></div>
</section>
<div class="slide-photo" role="img" aria-label="Photo of a family relaxing together at home with a laptop"></div>
<h1 class="slide-title">Mortgage<br>credit</h1>
<div class="slide-rule"></div>
<p class="slide-text">Cras sollicitudin<br>metus et tortor<br>rutrum sed.</p>
<a class="btn-orange" href="#">Read more</a>
<div class="dots"><i></i><i class="on"></i><i></i></div>

<nav class="main-nav">
  <a href="#"><svg viewBox="0 0 16 16"><path d="M8 1 0 8h2v7h4v-5h4v5h4V8h2z"/></svg>Home</a>
  <a href="#"><svg viewBox="0 0 16 16"><path d="M7 0h2l.4 2.2 1.6.7 1.9-1.3 1.4 1.4-1.3 1.9.7 1.6L16 7v2l-2.2.4-.7 1.6 1.3 1.9-1.4 1.4-1.9-1.3-1.6.7L9 16H7l-.4-2.2-1.6-.7-1.9 1.3-1.4-1.4 1.3-1.9-.7-1.6L0 9V7l2.2-.4.7-1.6-1.3-1.9 1.4-1.4 1.9 1.3 1.6-.7zM8 5a3 3 0 1 0 0 6 3 3 0 0 0 0-6z"/></svg>Services</a>
  <a href="#"><svg viewBox="0 0 16 16"><path d="M8 0a8 8 0 1 0 0 16A8 8 0 0 0 8 0zm1 12H7V7h2zm0-7H7V3h2z"/></svg>About Us</a>
  <a href="#"><svg viewBox="0 0 16 16"><path d="M0 2h16v12H0zm2 2v.4l6 4.2 6-4.2V4zm0 2.8V12h12V6.8L8 11z"/></svg>Contact Us</a>
</nav>

<aside class="promo">
  <h3>Lorem ipsum</h3>
  <p>Donec id cursus tortor. Nullam eget ligula sed augue aliquet pharetra.</p>
</aside>

<section class="news">
  <div class="news-intro">
    <svg viewBox="0 0 24 24" fill="none" stroke="#555" stroke-width="2"><path d="M14 5H4v15h15V10"/><path d="M20 2l2 2-9 9-3 1 1-3z" fill="#555"/></svg>
    <h2 class="section-title">Latest news</h2>
    <a class="btn-grey" href="#">View more</a>
  </div>
  <article class="news-item news-item-first">
    <div class="thumb" role="img" aria-label="Photo of a business meeting"></div>
    <div class="news-body">
      <div class="date">10.12.2012, 12:35</div>
      <h3 class="item-title">Mauris vel velit eget lorem</h3>
      <p>Donec id cursus tortor. Nullam eget ligula sed augue aliquet pharetra. Aenean egestas vestibulum leo, eget fermentum odio dignissim interdum massa.</p>
      <a class="more" href="#">Read more</a>
    </div>
  </article>
  <div class="news-sep"></div>
  <article class="news-item news-item-second">
    <div class="thumb alt" role="img" aria-label="Photo of a happy family outdoors"></div>
    <div class="news-body">
      <div class="date">10.12.2012, 12:35</div>
      <h3 class="item-title">Cras eget lacus sem, eu gravida</h3>
      <p>Donec id cursus tortor. Nullam eget ligula sed augue aliquet pharetra. Aenean egestas vestibulum leo, eget fermentum odio dignissim tristique.</p>
      <a class="more" href="#">Read more</a>
    </div>
  </article>
</section>

<h2 class="section-title services-title">Our services</h2>
<section>
  <article class="service service-one">
    <div class="service-photo" role="img" aria-label="Photo of business professionals"></div>
    <h3>Mauris vel velit eget lorem</h3>
    <p>Donec id cursus tortor. Nullam eget ligula sed augue aliquet pharetra. Aenean egestas vestibulum leo, eget fermentum odio dignissim.</p>
  </article>
  <article class="service service-two">
    <div class="service-photo warm" role="img" aria-label="Photo of a family on a sofa"></div>
    <h3>Integer ut tellus a diam porta pulvinar</h3>
    <p>Quisque feugiat justo nec sapien feugiat vitae elementum massa sollicitudin. Fusce sodales dui vel risus vulputate adipiscing.</p>
  </article>
  <article class="service service-three">
    <div class="service-photo cool" role="img" aria-label="Photo of a business team"></div>
    <h3>Quisque a nunc ante, non dui</h3>
    <p>Donec id cursus tortor. Nullam eget ligula sed augue aliquet pharetra. Aenean egestas vestibulum leo, eget fermentum odio dignissim.</p>
  </article>
</section>
<div class="services-rule"></div>

<section class="partners">
  <span class="partners-label">Our partners</span>
  <span class="partner">Norvane</span>
  <span class="partner">Castrel Mutual</span>
  <span class="partner">Hollbeck Bank</span>
  <span class="partner">Sarrow</span>
</section>

<footer class="site-footer">
  <div class="badge" role="img" aria-label="Accreditation badge"></div>
  <nav class="footer-nav">
    <a href="#">Home</a><a href="#">Services</a><a href="#">About Us</a><a href="#">Contact Us</a><a href="#">Privacy</a>
  </nav>
  <p class="copyright">Copyright 2012 Tallowen Lending Group. All Right Reserved.</p>
  <a class="to-top" href="#">Back to top</a>
</footer>

</body>
</html>
```